Linen Sparrow- Hand made fashion accessories

Linen sparrow is a new business that will be selling hand made fashion accessories for women such as bags, baskets, knecklaces etc. The items are all hand made from Africa. I would like natural colors leaning more to the cardboard rustic look. I would like the card to look simple but elegant at the same time.

Industry/Entity Type

Business

Contact Information for Business Card

www.linensparrow-example.com.au
sales@linensparrow-example.com.au
Tel: 0427586302

Font styles to use
Decorative
Script

Requirements
Must have
• Earthy and rustic colours. Straw, cardboard etc. Fine black cursive print. One side of card only name
• second side website, email and tel.
Should not have
• No need to have any description of what business sells or does. No pictures of anything.

```html
<!DOCTYPE html>
<html lang="en">
<head>
<meta charset="utf-8">
<title>Linen Sparrow – Business Card</title>
<link rel="stylesheet" href="https://fonts.googleapis.com/css2?family=Allura&family=Questrial&display=swap">
<style>
  :root {
    --backdrop: #8c8274;
    --card-stock: #d9c4a0;
    --frame-line: #2b2118;
    --ink-script: #1a140e;
    --ink-contact: #4d3d2c;
    --ring-line: #a88f69;
  }
  * { margin: 0; padding: 0; box-sizing: border-box; }
  html, body {
    width: 1105px;
    height: 1200px;
    overflow: hidden;
    background: var(--backdrop);
  }
  .canvas {
    position: relative;
    width: 1105px;
    height: 1200px;
  }
  .card {
    position: absolute;
    left: 183px;
    width: 745px;
    height: 424px;
    background: var(--card-stock);
  }
  .card--front { top: 120px; }
  .card--back { top: 637px; }
  .card__frame {
    position: absolute;
    inset: 14px;
    border: 1.5px solid var(--frame-line);
    border-radius: 32px;
  }
  .card__name {
    position: absolute;
    left: 0;
    right: 0;
    top: 180px;
    text-align: center;
    font-family: "Allura", cursive;
    font-size: 62px;
    line-height: 1;
    color: var(--ink-script);
  }
  .brand {
    position: absolute;
    left: 274px;
    top: 60px;
    width: 194px;
    height: 194px;
    display: flex;
    align-items: center;
    justify-content: center;
  }
  .brand__ring {
    position: absolute;
    inset: 0;
  }
  .brand__name {
    position: relative;
    font-family: "Questrial", sans-serif;
    font-size: 26px;
    line-height: 1.2;
    text-align: center;
    color: var(--ink-script);
  }
  .contact {
    position: absolute;
    left: 0;
    right: 0;
    top: 273px;
    list-style: none;
    text-align: center;
    font-family: "Questrial", sans-serif;
    font-size: 19.5px;
    line-height: 29.5px;
    color: var(--ink-contact);
  }
</style>
</head>
<body>
  <main class="canvas">
    <section class="card card--front" aria-label="Card front">
      <div class="card__frame"></div>
      <p class="card__name">Amara Cole</p>
    </section>

    <section class="card card--back" aria-label="Card back">
      <div class="card__frame"></div>
      <div class="brand">
        <svg class="brand__ring" viewBox="0 0 194 194" aria-hidden="true">
          <circle cx="97" cy="97" r="96" fill="none" stroke="var(--ring-line)" stroke-width="1.2"/>
        </svg>
        <p class="brand__name">Linen<br>Sparrow</p>
      </div>
      <ul class="contact">
        <li>Tel: 0427586302</li>
        <li>sales@linensparrow-example.com.au</li>
        <li>www.linensparrow-example.com.au</li>
      </ul>
    </section>
  </main>
</body>
</html>
```